Brightloom Reach - Business Card

We need a business card for a Social Media Marketing company that specializes in online marketing for small businesses in Canada using common Social Media platforms such as Instagram, Facebook, Snapchat & Twitter.

I have uploaded a copy of our logo which I would like utilized in the business card. We would like the business card to be modern yet classy design.

Our website is www.brightloomreach.ca

Industry/Entity Type

Marketing

Contact Information for Business Card

Email: info@brightloomreach.ca
Website: www.brightloomreach.ca
Telephone: 604-352-9081

Colors

Designer to choose colors to be used in the design.

Requirements
Must have
• Social Media icons on reverse
• Please add some designs with color.

```html
<!DOCTYPE html>
<html lang="en">
<head>
<meta charset="utf-8">
<title>Brightloom Reach – Business Card</title>
<link rel="stylesheet" href="https://fonts.googleapis.com/css2?family=Roboto+Condensed:wght@400;700&display=swap">
<style>
  :root {
    --stage: #0c0c0c;
    --charcoal: #2e2f30;
    --charcoal-light: #3b3d3e;
    --slate: #3e4041;
    --mist: #e7e7e5;
    --cream: #f9f7f2;
    --ink: #2f3031;
    --white: #ffffff;
  }
  * { box-sizing: border-box; margin: 0; padding: 0; }
  html, body {
    width: 1200px; height: 1000px; overflow: hidden;
    background: var(--stage);
    font-family: "Roboto Condensed", "Arial Narrow", sans-serif;
  }
  .canvas { position: relative; width: 1200px; height: 1000px; }

  .card {
    position: absolute; width: 560px; height: 320px;
    overflow: hidden; box-shadow: 0 12px 30px rgba(0,0,0,.6);
  }
  .card svg.card-bg { position: absolute; inset: 0; }

  /* Back of card */
  .card-back { left: 50px; top: 150px; background: var(--charcoal); }
  .back-brand {
    position: absolute; left: 0; right: 0; top: 118px;
    text-align: center; color: var(--white);
    font-weight: 700; font-size: 30px; line-height: 1; letter-spacing: .5px;
    text-transform: uppercase; white-space: nowrap;
  }
  .social-row {
    position: absolute; left: 0; right: 0; top: 166px;
    display: flex; justify-content: center; gap: 14px;
  }
  .social-dot { width: 24px; height: 24px; border-radius: 50%; background: var(--white); }

  /* Front of card */
  .card-front { left: 600px; top: 510px; background: var(--cream); }
  .holder {
    position: absolute; left: 40px; top: 44px; color: var(--white);
    white-space: nowrap;
  }
  .holder-name { font-weight: 700; font-size: 19px; line-height: 1.2; letter-spacing: .5px; text-transform: uppercase; }
  .holder-role { font-weight: 400; font-size: 15px; line-height: 1.2; letter-spacing: .5px; text-transform: uppercase; margin-top: 2px; }
  .front-brand {
    position: absolute; right: 30px; top: 128px; width: 160px;
    text-align: center; color: var(--ink);
    font-weight: 700; font-size: 24px; line-height: 1.05; text-transform: uppercase;
  }
  .contact-row {
    position: absolute; left: 28px; right: 28px; bottom: 36px;
    display: flex; justify-content: space-between; align-items: baseline; gap: 20px;
    color: var(--ink); font-size: 14px; line-height: 1; letter-spacing: .3px;
    text-transform: uppercase; white-space: nowrap;
  }
  .contact-web { font-weight: 700; font-size: 15px; }
</style>
</head>
<body>
<main class="canvas">

  <section class="card card-back" aria-label="Card back">
    <svg class="card-bg" width="560" height="320" viewBox="0 0 560 320" aria-hidden="true">
      <polygon points="320,0 560,0 560,320 86,320" fill="var(--charcoal-light)"/>
    </svg>
    <p class="back-brand">Brightloomreach</p>
    <div class="social-row" aria-label="Social media channels">
      <span class="social-dot"></span>
      <span class="social-dot"></span>
      <span class="social-dot"></span>
      <span class="social-dot"></span>
    </div>
  </section>

  <section class="card card-front" aria-label="Card front">
    <svg class="card-bg" width="560" height="320" viewBox="0 0 560 320" aria-hidden="true">
      <rect x="14" y="14" width="532" height="212" fill="var(--mist)"/>
      <polygon points="14,14 380,14 265,226 14,226" fill="var(--slate)"/>
    </svg>
    <div class="holder">
      <p class="holder-name">Daniel Hartley</p>
      <p class="holder-role">Manager</p>
    </div>
    <p class="front-brand">Brightloom Reach</p>
    <div class="contact-row">
      <span class="contact-phone">604-352-9081</span>
      <span class="contact-mail">info@brightloomreach.ca</span>
      <span class="contact-web">www.brightloomreach.ca</span>
    </div>
  </section>

</main>
</body>
</html>
```